Restwell/Snoring Business - Requires Website - Australia

We are seeking a simple to maintain website for our sleep business. The health care business provides diagnostic and treatment solutions for snoring, sleep disorders and other respiratory problems.

Ideally, colours to match the company logo (attached).

The page must be built using WORDPRESS.

Ideally site will have a home page outlining the business, with 5 sub pages - being "Diagnosis" "Treatment Options", "Prodcuts", "About Us", "Contact Us"

The site home page should include a large picture on the home page.

The "Treatment Options" and "Diagnosis" pages must include:
Allow for a few pictures with assocaited text, plus space for some embeded youtube videos.

"Prodcuts" page should have the ability to show 3-4 products across the page with text below.. that can include external URL to products

The "About Us" page must include:
1. a Map (google map) to identify the various locations. There are 6 in total.
2. A Section to describe our doctors/staff - allow for a picture and some text

The "Contact Us" page must include:
email form
telephone details

The overall design should have a clean and medical/safe feeling

Target Market(s)

People who snore and those with sleeping and respiratory disorders

Industry/Entity Type

Health Care

Coding

Coded - Design and coding required

Number of Pages Required

5+ page

Colors

Designer to choose colors to be used in the design.

Requirements
Must have
• The page must be built using WORDPRESS.
• Ideally site will have a home page outlining the business, with 5 sub pages - being "Diagnosis" "Treatment Options", "Prodcuts", "About Us", "Contact Us"
• The site home page should include a large picture on the home page.
• The "Treatment Options" and "Diagnosis" pages must include:
• Allow for a few pictures with assocaited text, plus space for some embeded youtube videos.
• "Prodcuts" page should have the ability to show 3-4 products across the page with text below.. that can include external URL to products
• The "About Us" page must include:
• 1. a Map (google map) to identify the various locations. There are 6 in total.
• 2. A Section to describe our doctors/staff - allow for a picture and some text
• The "Contact Us" page must include:
• email form
• telephone details
• Pictures must be licenced or free to use
Nice to have
• Home page pictures showing people sleeping well, snoring or fresh air (landscape) type transition pictures (at least 3).
Should not have
• Not to look cheap
• This is a high end healthcare business, so must look that way

```html
<!DOCTYPE html>
<html lang="en">
<head>
<meta charset="utf-8">
<title>Restwell Australia – Sleep Diagnosis &amp; Treatment</title>
<link rel="stylesheet" href="https://fonts.googleapis.com/css2?family=Roboto+Condensed:wght@300;700&family=Source+Sans+3:wght@400;600;700&display=swap">
<style>
  :root {
    --navy: #1b4a7e;
    --nav: #1d4d82;
    --band: #174a7c;
    --sky: #8fb0da;
    --btn-soft: #9cb5d9;
    --ink: #2b2b2b;
    --muted: #555;
    --grey-bg: #e1e1e1;
    --grey-bar: #d4d4d4;
    --line: #a9bcd9;
    --white: #fff;
  }
  * { box-sizing: border-box; margin: 0; padding: 0; }
  html, body { width: 1200px; height: 1170px; overflow: hidden; }
  body { font-family: "Source Sans 3", "Source Sans Pro", sans-serif; color: var(--ink); background: var(--white); position: relative; }

  .site-header { position: absolute; top: 0; left: 0; width: 1200px; height: 126px; }
  .brand { position: absolute; left: 73px; top: 28px; display: flex; align-items: center; gap: 10px; }
  .brand-dot { width: 18px; height: 18px; border-radius: 50%; background: var(--navy); }
  .brand-name { font-size: 44px; font-weight: 700; color: var(--navy); letter-spacing: -1px; }
  .header-arc { position: absolute; left: 775px; top: 0; }
  .call { position: absolute; left: 830px; top: 44px; text-align: right; width: 184px; }
  .call-label { font-size: 14px; color: #333; margin-right: 38px; }
  .call-number { font-size: 22px; font-weight: 700; color: var(--navy); display: flex; align-items: center; gap: 6px; justify-content: flex-end; }
  .header-divider { position: absolute; left: 1031px; top: 37px; width: 1px; height: 54px; background: #ccc; }
  .social { display: flex; gap: 3px; }
  .social-icon { width: 27px; height: 27px; border: 2px solid #aaa; border-radius: 50%; }
  .header-social { position: absolute; left: 1042px; top: 51px; }

  .main-nav { position: absolute; top: 126px; left: 0; width: 1200px; height: 43px; background: var(--nav); display: flex; justify-content: center; }
  .main-nav a { color: var(--white); text-decoration: none; font-size: 17px; font-weight: 600; letter-spacing: .3px; line-height: 43px; padding: 0 31px; border-left: 1px solid rgba(255,255,255,.22); }
  .main-nav a:first-child { border-left: 0; }

  .hero { position: absolute; top: 169px; left: 0; width: 1200px; height: 499px; }
  .hero-photo { position: absolute; inset: 0; background: linear-gradient(100deg, #f4f3f2 0%, #efe9e5 35%, #e9d2c2 55%, #eadfd9 75%, #f2f0ef 100%); }
  .hero-copy { position: absolute; left: 73px; top: 157px; width: 460px; }
  .hero-title { font-family: "Roboto Condensed", sans-serif; font-size: 39px; line-height: 34px; font-weight: 700; color: var(--navy); }
  .hero-title span { display: block; font-weight: 300; color: #2b2b2b; }
  .hero-text { margin-top: 20px; font-size: 17px; line-height: 23px; color: #333; }
  .btn { display: inline-block; font-size: 15px; color: var(--white); text-decoration: none; border-radius: 2px; padding: 0 14px; line-height: 30px; }
  .btn-primary { background: var(--navy); margin-top: 24px; }
  .btn-soft { background: var(--btn-soft); }

  .intro-band { position: absolute; top: 668px; left: 0; width: 1200px; height: 124px; background: var(--band); border-bottom: 3px solid var(--sky); }
  .intro-band h2 { position: absolute; left: 77px; top: 20px; color: var(--white); font-size: 29px; font-weight: 700; line-height: 33px; }
  .intro-band h2 span { display: block; font-weight: 400; font-size: 26px; }
  .video-frame { position: absolute; left: 666px; top: 573px; width: 360px; height: 207px; border: 4px solid var(--white); box-shadow: 0 0 3px rgba(0,0,0,.3); background: linear-gradient(110deg, #c8b9a8 0%, #efeae4 40%, #8a5a36 70%, #d9d5d0 100%); }
  .play { position: absolute; left: 164px; top: 82px; width: 40px; height: 36px; border-radius: 50%; background: rgba(255,255,255,.9); }
  .play::after { content: ""; position: absolute; left: 15px; top: 10px; border-left: 13px solid var(--navy); border-top: 8px solid transparent; border-bottom: 8px solid transparent; }

  .welcome { position: absolute; top: 792px; left: 0; width: 1200px; height: 196px; text-align: center; }
  .welcome h2 { margin-top: 40px; font-size: 23px; font-weight: 400; color: #222; }
  .welcome h2 em { font-style: normal; color: var(--navy); }
  .welcome h2::after { content: ""; display: block; width: 86px; height: 1px; background: #999; margin: 5px auto 0; }
  .welcome p { width: 1060px; margin: 13px auto 0; font-size: 15px; line-height: 22px; color: var(--muted); }
  .welcome .btn { margin-top: 13px; }

  .site-footer { position: absolute; top: 988px; left: 0; width: 1200px; height: 136px; background: var(--grey-bg); border-top: 3px solid var(--line); }
  .footer-social { position: absolute; left: 73px; top: 29px; display: flex; align-items: center; gap: 9px; font-size: 17px; color: #333; }
  .footer-contact { position: absolute; left: 73px; top: 83px; width: 330px; display: flex; gap: 12px; font-size: 15px; color: #333; white-space: nowrap; }
  .footer-contact span { display: flex; align-items: center; gap: 8px; }
  .contact-icon { width: 26px; height: 26px; border: 2px solid #999; border-radius: 50%; display: flex; align-items: center; justify-content: center; flex: none; }
  .footer-links { position: absolute; left: 413px; top: 28px; width: 266px; height: 82px; border-left: 1px solid #bbb; border-right: 1px solid #bbb; padding-left: 19px; display: grid; grid-template-columns: 144px 100px; row-gap: 11px; }
  .footer-links a { font-size: 15px; color: #333; text-decoration: none; line-height: 20px; white-space: nowrap; }
  .footer-links a::before { content: ""; display: inline-block; border-left: 4px solid #555; border-top: 4px solid transparent; border-bottom: 4px solid transparent; margin-right: 5px; }
  .newsletter { position: absolute; left: 704px; top: 28px; width: 422px; }
  .newsletter h3 { font-size: 19px; font-weight: 600; color: #111; }
  .newsletter p { font-size: 15px; color: #333; margin-top: 2px; }
  .subscribe { display: flex; margin-top: 9px; }
  .subscribe input { flex: 1; height: 34px; border: 0; padding: 0 12px; font: 15px "Source Sans 3", sans-serif; color: #555; }
  .subscribe button { width: 108px; background: var(--navy); color: var(--white); border: 0; font: 700 15px "Source Sans 3", sans-serif; }

  .legal { position: absolute; top: 1124px; left: 0; width: 1200px; height: 46px; background: var(--grey-bar); text-align: center; line-height: 46px; font-size: 16px; color: #333; }
  .legal a { color: #333; text-decoration: none; }
  .legal .sep { margin: 0 6px; }
</style>
</head>
<body>
  <header class="site-header">
    <div class="brand"><span class="brand-dot"></span><span class="brand-name">Restwell</span></div>
    <svg class="header-arc" width="140" height="126" viewBox="0 0 140 126" aria-hidden="true">
      <path d="M6 0 C 14 50, 50 105, 135 126 L 128 126 C 42 108, 4 55, 0 0 Z" fill="#8fb0da"/>
    </svg>
    <div class="call">
      <div class="call-label">Call Us Today On</div>
      <div class="call-number">
        <svg width="20" height="20" viewBox="0 0 24 24" aria-hidden="true"><path fill="#1b4a7e" d="M6.6 10.8a15.1 15.1 0 0 0 6.6 6.6l2.2-2.2c.3-.3.7-.4 1-.2 1.1.4 2.3.6 3.6.6.6 0 1 .4 1 1V20c0 .6-.4 1-1 1A17 17 0 0 1 3 4c0-.6.4-1 1-1h3.5c.6 0 1 .4 1 1 0 1.3.2 2.5.6 3.6.1.3 0 .7-.2 1z"/></svg>
        1000 555 0188
      </div>
    </div>
    <div class="header-divider"></div>
    <div class="social header-social"><span class="social-icon"></span><span class="social-icon"></span><span class="social-icon"></span></div>
  </header>

  <nav class="main-nav">
    <a href="#">HOME</a><a href="#">DIAGNOSIS</a><a href="#">TREATMENT OPTIONS</a><a href="#">PRODCUTS</a><a href="#">ABOUT US</a><a href="#">CONTACT US</a>
  </nav>

  <section class="hero">
    <div class="hero-photo" role="img" aria-label="A couple in bed: the man snores while the woman, kept awake, covers her ear"></div>
    <div class="hero-copy">
      <h1 class="hero-title">Different Treatment Options<span>to Suit Your Needs</span></h1>
      <p class="hero-text">Lorem ipsum dolor sit amet, consectetur adipiscing elit, sed do eiusmod tempor incididunt ut labore et dolore magna aliqua. Ut enim ad minim veniam, quis nostrud exercitation ullamco laboris nisi ut aliquip ex ea commodo.</p>
      <a class="btn btn-primary" href="#">Read More</a>
    </div>
  </section>

  <section class="intro-band">
    <h2>A Specialist run Centre Dedicated to the<span>Diagnosis, and Treatment of all Sleep Disorders</span></h2>
  </section>
  <div class="video-frame" role="img" aria-label="Video thumbnail: a woman sleeping with a CPAP mask beside the machine">
    <span class="play"></span>
  </div>

  <section class="welcome">
    <h2>WELCOME TO <em>RESTWELL AUSTRALIA</em></h2>
    <p>Lorem ipsum dolor sit amet, consectetur adipiscing elit, sed do eiusmod tempor incididunt ut labore et dolore magna aliqua. Ut enim ad minim veniam, quis nostrud exercitation ullamco laboris nisi ut aliquip ex ea commodo consequat. Duis aute irure dolor in reprehenderit in voluptate velit esse cillum dolore eu fugiat nulla pariatur.</p>
    <a class="btn btn-soft" href="#">Read More</a>
  </section>

  <footer class="site-footer">
    <div class="footer-social">Social:<div class="social"><span class="social-icon"></span><span class="social-icon"></span><span class="social-icon"></span></div></div>
    <div class="footer-contact">
      <span><span class="contact-icon"><svg width="13" height="13" viewBox="0 0 24 24" aria-hidden="true"><path fill="#777" d="M6.6 10.8a15.1 15.1 0 0 0 6.6 6.6l2.2-2.2c.3-.3.7-.4 1-.2 1.1.4 2.3.6 3.6.6.6 0 1 .4 1 1V20c0 .6-.4 1-1 1A17 17 0 0 1 3 4c0-.6.4-1 1-1h3.5c.6 0 1 .4 1 1 0 1.3.2 2.5.6 3.6.1.3 0 .7-.2 1z"/></svg></span>1000 555 0188</span>
      <span><span class="contact-icon"><svg width="13" height="10" viewBox="0 0 13 10" aria-hidden="true"><rect x="0.5" y="0.5" width="12" height="9" fill="none" stroke="#777"/><path d="M.5 .5 L6.5 5.5 L12.5 .5" fill="none" stroke="#777"/></svg></span>info@restwell.example</span>
    </div>
    <div class="footer-links">
      <a href="#">Home</a><a href="#">Prodcuts</a>
      <a href="#">Diagnosis</a><a href="#">About Us</a>
      <a href="#">Treatment Options</a><a href="#">Contact Us</a>
    </div>
    <div class="newsletter">
      <h3>Subscribe Newsletter</h3>
      <p>Join the be Restwell for regular updates and information.</p>
      <form class="subscribe"><input type="email" placeholder="Enter your email address"><button type="button">SUBSCRIBE</button></form>
    </div>
  </footer>

  <div class="legal">© 2017 Restwell. All Rights Reserved.<span class="sep">|</span><a href="#">Terms of Use</a><span class="sep">|</span><a href="#">Privacy Policy</a></div>
</body>
</html>
```